Warmloft van wrap design

Hi!

We are a domestic gas engineering company. Installing , repairing and servicing gas appliances in homes.

We have been running for two years and have recently taken on more staff. It’s now time to think about looking more professional and having our fleet looking smart.

Information that is needed to be advertised, phone number 01632 958274, email info@warmloft.example.co.uk, website www.warmloft.example.co.uk, logos such as fuel secure roster, Pembury Halvik credited installer, and Chatterbook (a QR code would be lovely)

We are also a Pembury Halvik accredited installer and we can offer 12yr warranties on certain boilers.

Our van currently reads:
Installation,
Servicing,
Repair,
Boilers, Fires and Gas Appliances

Which is useful information for customers.

Our colours are orange and blue to represent warmth and water. Our new logo has pipes and flames in it.

We use a white Dunmore carrier select short wheel base van

Our website is warmloft.example.co.uk
Updates

We feel like some of the designs don’t meet the brief. We have stayed we want to move away from the house logo and therefore don’t want it on the new designs. We have one design we really like but we would like a few other designs which match the brief before we make a decision. Thanks

Target Market(s)

Home owners and landlords

Industry/Entity Type

Gas Engineering, Heating

Font styles to use
Other font styles liked:
• See logo fonts

Colors
0054AA
0677BA
7BADD7
CADEEF
E8F1F8
F0912C
F2A743
F7CA91
FBE8D2
FDF5EE

Requirements
Must have
• Our design must show warmth as that’s what we do, warm up homes!
Nice to have
• We like the idea of a full van wrap but we are happy to see other designs which may only include a partial wrap.
Should not have
• Not too busy or overwhelming with images

```html
<!DOCTYPE html>
<html lang="en">
<head>
<meta charset="utf-8">
<title>Warmloft van wrap concepts</title>
<link href="https://fonts.googleapis.com/css2?family=Poppins:wght@400;500;600;700&display=swap" rel="stylesheet">
<style>
  :root{
    --blue:#0054AA;
    --blue-mid:#0677BA;
    --orange:#F0912C;
    --orange-light:#F2A743;
    --orange-deep:#E8561E;
    --teal-text:#0B5C73;
    --badge:#F2C200;
    --white:#FFFFFF;
    --canvas:#F4F5F7;
    --panel-edge:#D6DCE4;
  }
  *{margin:0;padding:0;box-sizing:border-box}
  html,body{width:1200px;height:1200px;overflow:hidden;background:var(--canvas);font-family:"Poppins",sans-serif}
  .wrap-panel{position:absolute;left:50px;width:1100px;height:460px;background:var(--white);border:1px solid var(--panel-edge);border-radius:18px;overflow:hidden}
  .concept-a{top:60px}
  .concept-b{top:660px}
  .panel-art{position:absolute;inset:0}
  .abs{position:absolute}

  .brand-name{font-weight:700;line-height:1}
  .tagline{font-weight:600;text-transform:uppercase;white-space:nowrap}
  .phone{font-weight:600;font-size:26px;letter-spacing:.5px;line-height:1.25}
  .web,.email{font-size:14px;line-height:1.5;white-space:nowrap}
  .web b{font-weight:700}

  /* concept A */
  .a-brand{left:380px;top:70px;width:360px;text-align:center}
  .a-brand .brand-name{font-size:64px;color:var(--orange-deep)}
  .a-brand .tagline{font-size:11.5px;color:var(--blue);letter-spacing:2.4px;margin-top:4px}
  .a-contact{left:190px;top:205px;color:var(--teal-text)}
  .a-contact .web{color:var(--orange-deep)}
  .badge-row{left:36px;top:212px;display:flex;gap:8px;align-items:center}
  .badge-plain{width:22px;height:22px;background:var(--badge);border-radius:3px}
  .social-name{font-size:11px;font-weight:500;color:var(--blue);display:flex;align-items:center;gap:4px}
  .social-name i{display:block;width:10px;height:10px;background:var(--blue)}
  .a-services{left:430px;top:205px;display:flex;gap:14px;color:var(--teal-text)}
  .service-main{font-size:20px;line-height:1.3}
  .service-list{border-left:1px solid var(--teal-text);padding-left:7px;font-size:11px;line-height:1.35;margin-top:4px}

  /* concept B */
  .b-strip-text{left:430px;top:131px;transform:rotate(-9.8deg);transform-origin:left top;font-size:14px;line-height:24px;font-weight:600;letter-spacing:2px;color:var(--white);text-transform:uppercase;white-space:nowrap}
  .b-strip-text span{color:var(--blue);margin:0 5px}
  .b-brand{left:480px;top:195px;transform:rotate(-9.8deg);transform-origin:left top}
  .b-brand .brand-name{font-size:72px;color:var(--white)}
  .b-brand .tagline{font-size:14px;color:var(--white);letter-spacing:3.5px;margin-top:4px}
  .b-contact{left:205px;top:252px;color:var(--white)}
  .b-contact .web{color:var(--orange-light)}
</style>
</head>
<body>

<section class="wrap-panel concept-a" aria-label="Partial wrap concept">
  <svg class="panel-art" viewBox="0 0 1100 460" aria-hidden="true">
    <defs>
      <linearGradient id="sillTone" x1="0" y1="0" x2="1" y2="0">
        <stop offset="0" stop-color="#F0912C"/>
        <stop offset="1" stop-color="#E8561E"/>
      </linearGradient>
    </defs>
    <path d="M0 330 Q500 318 1100 300 L1100 375 L0 385 Z" fill="var(--blue)"/>
    <rect x="0" y="392" width="1100" height="40" fill="url(#sillTone)"/>
    <path d="M990 0 L1100 0 L1100 300 L960 305 Q1030 220 1010 130 Q995 60 990 0 Z" fill="var(--blue)"/>
  </svg>
  <div class="abs" role="img" aria-label="Large flame graphic in orange" style="left:820px;top:20px;width:190px;height:290px;background:linear-gradient(to top,#E8561E,#F0912C);border-radius:50% 50% 40% 40% / 60% 60% 30% 30%"></div>

  <div class="abs a-brand">
    <div class="brand-name">Warmloft</div>
    <div class="tagline">Your home heating specialists</div>
  </div>

  <div class="abs badge-row">
    <div class="badge-plain" aria-label="Fuel secure roster badge"></div>
    <div class="social-name"><i></i>Chatterbook</div>
  </div>

  <div class="abs a-contact">
    <div class="phone">01632 958274</div>
    <div class="web">www.<b>warmloft</b>.example.co.uk</div>
    <div class="email">info@warmloft.example.co.uk</div>
  </div>

  <div class="abs a-services">
    <div class="service-main">Installation<br>Servicing<br>Repairs</div>
    <div class="service-list">Fires<br>Boilers<br>Cookers<br>Plumbing<br>Radiators</div>
  </div>
</section>

<section class="wrap-panel concept-b" aria-label="Diagonal band wrap concept">
  <svg class="panel-art" viewBox="0 0 1100 460" aria-hidden="true">
    <polygon points="0,200 1100,10 1100,38 0,228" fill="var(--orange)"/>
    <polygon points="0,236 1100,46 1100,230 0,420" fill="var(--blue)"/>
    <polygon points="0,428 1100,238 1100,262 0,452" fill="var(--orange-deep)"/>
  </svg>

  <div class="abs b-strip-text">Fires<span>•</span>Boilers<span>•</span>Cookers<span>•</span>Plumbing<span>•</span>Radiators</div>

  <div class="abs b-brand">
    <div class="brand-name">Warmloft</div>
    <div class="tagline">Your home heating specialists</div>
  </div>

  <div class="abs b-contact">
    <div class="phone">01632 958274</div>
    <div class="web">www.<b>warmloft</b>.example.co.uk</div>
    <div class="email">info@warmloft.example.co.uk</div>
  </div>
</section>

</body>
</html>
```